Plakate für Haushaltshilfen und Alltagsbegleiter
Zielgruppe
Wir bieten haushaltsnahe Dienstleistungen (Haushaltshilfen und Altgasbegleiter) für Personen mit einem Pflegegrad 1 - 5 an.
Zielgruppe sind Personen mit einem Pflegegrad 1 - 5. Hauptsächlich ältere Menschen die Unterstützung/Betreuung im Alltag und Haushalt benötigen.
Aufgabenstellung
Wir benötigen für unsere Büroräume eine Fensterbeschriftung. Es handelt sich hier um 5 Fenster (Glasflächen) und eine Glastür. Die Vorgabe ist, dass von außen zu erkennen ist dass sich um alle Räumlichkeiten um unsere (Firma Lindwerk) Räumlichkeiten handelt. Desweiteren soll auch unser Angebot erkennbar sein.
Unser Angebot enthält: Haushaltshilfen und Alltagsbegleiter
- kostenlose Haushaltshilfe ab Pflegegrad 1
- Abrechnung mit allen Kostenträgern
Da wir keine Schilder an die Fassade anbringen können, müßen die Glasflächen dafür genutzt werden um zum Einen uns als Firma erkennbar zu machen und zum anderen unser Angebot kurz zu präsentieren.
Uns ist wichtig dass unser Logo verwendet wir und auch unsere Farben.
Desweiteren sollten an den Fenstern auch teilweise eine Sichtschutz nach innen, angebracht werden, aber eben nur teilweise also nicht das ganzen Fenster z.Bsp. mit einer Blickdichten Folie überziehen, sondern in Augenhöhe wenn Fußgänger vorbei laufen.

```html
<!DOCTYPE html>
<html lang="de">
<head>
<meta charset="utf-8">
<title>Lindwerk – Fensterplakate</title>
<link rel="stylesheet" href="https://fonts.googleapis.com/css2?family=Cinzel:wght@600;700&family=Poppins:wght@400;500;700&family=Kalam:wght@700&display=swap">
<style>
:root{
  --red:#c8202e;
  --red-dark:#a3151f;
  --charcoal:#3d3d40;
  --ink:#4a4a4d;
  --white:#ffffff;
  --sweep:#e4e4e6;
  --bg:#c4c4c6;
  --frame:#9c9c9e;
  --frame-light:#b2b2b4;
}
*{box-sizing:border-box;margin:0;padding:0}
html,body{width:1200px;height:2234px;overflow:hidden;background:var(--bg)}
body{position:relative;font-family:'Poppins',sans-serif}
.frame{position:absolute;background:linear-gradient(180deg,var(--frame-light),var(--frame));box-shadow:0 2px 4px rgba(0,0,0,.15)}
.frame-top{left:56px;top:410px;width:1088px;height:495px}
.frame-bottom{left:56px;top:1040px;width:1088px;height:578px}
.frame-bottom-ext{left:411px;top:1600px;width:378px;height:223px}
.poster,.panel{position:absolute;overflow:hidden}
.poster{background:var(--white)}
.panel{background:var(--charcoal)}
.shapes{position:absolute;inset:0;width:100%;height:100%}
.photo{position:absolute}
.brand{position:absolute;display:flex;align-items:center;gap:8px}
.brand-mark{width:40px;height:40px;border-radius:50%;border:4px solid var(--red);flex:none}
.brand-name{font-family:'Cinzel',serif;font-weight:600;font-size:27px;line-height:1;color:var(--ink);letter-spacing:.5px}
.brand-sub{font-family:'Cinzel',serif;font-weight:600;font-size:9.5px;color:var(--red);letter-spacing:.6px;margin-top:3px}
.brand.on-red .brand-mark{border-color:var(--white)}
.brand.on-red .brand-name{color:var(--white)}
.brand.on-red .brand-sub{color:var(--white)}
.headline{position:absolute;left:0;right:0;text-align:center;font-family:'Cinzel',serif;font-weight:700;color:var(--white);font-size:19px;line-height:1.05}
.cta{position:absolute;left:0;right:0;text-align:center;color:var(--white)}
.cta-label{font-size:9.5px;font-weight:500}
.phone{display:flex;align-items:center;justify-content:center;gap:6px;font-weight:700;font-size:28px;line-height:1.1}
.phone-icon{width:20px;height:20px;flex:none}
.url{font-size:10.5px;font-weight:500;letter-spacing:3.5px}
.script{position:absolute;font-family:'Kalam',cursive;font-weight:700;color:var(--red);line-height:.95;transform:rotate(-8deg)}
.lead{position:absolute;font-family:'Cinzel',serif;font-weight:700;color:var(--red);line-height:1.05}
.small{position:absolute;font-size:8px;line-height:1.35;color:var(--ink)}
.contact-label{font-family:'Cinzel',serif;font-weight:700;font-size:9px;color:var(--red);letter-spacing:.5px}
.contact-num{display:flex;align-items:center;gap:5px;font-weight:700;font-size:20px;color:var(--ink);line-height:1.1}
</style>
</head>
<body>

<!-- top row -->
<div class="frame frame-top">

  <section class="poster" style="left:22px;top:20px;width:333px;height:452px">
    <div class="photo" role="img" aria-label="Foto: Frau mit Putzhandschuhen klatscht mit einem Kind ab" style="left:0;top:170px;width:333px;height:200px;background:linear-gradient(135deg,#efe6da,#d9c3a8 60%,#f3ede4)"></div>
    <svg class="shapes" viewBox="0 0 333 452" aria-hidden="true">
      <path d="M0,98 C90,72 230,70 333,86 L333,178 C240,192 110,170 0,190 Z" fill="var(--charcoal)"/>
      <path d="M0,186 C110,168 240,188 333,174 L333,180 C240,194 110,174 0,194 Z" fill="var(--red)"/>
      <path d="M0,352 C120,320 230,338 333,300 L333,322 C230,356 120,336 0,366 Z" fill="var(--sweep)"/>
      <path d="M0,366 C120,336 230,356 333,322 L333,452 L0,452 Z" fill="var(--red)"/>
    </svg>
    <div class="brand" style="left:50px;top:22px"><span class="brand-mark"></span><div><div class="brand-name">LINDWERK</div><div class="brand-sub">HAUSHALTSHILFEN &amp; MEHR</div></div></div>
    <div class="headline" style="top:118px">HAUSHALTSHILFEN UND<br>ALLTAGSBEGLEITER</div>
    <div class="script" style="left:170px;top:200px;font-size:22px">Wir Sind<br>für Sie da!</div>
    <div class="cta" style="top:380px">
      <div class="cta-label">Buchen Sie gleich einen Termin:</div>
      <div class="phone"><svg class="phone-icon" viewBox="0 0 20 20"><circle cx="10" cy="10" r="10" fill="#fff"/><path d="M6.2,5.2l2,-.4 1.2,2.6-1.3,1c.6,1.3 1.6,2.3 2.9,2.9l1-1.3 2.6,1.2-.4,2c-4.5,.3-8.3,-3.5-8,-8z" fill="var(--red)"/></svg>0711 98 76 54 32</div>
      <div class="url">www.lindwerk-hilfe.de</div>
    </div>
  </section>

  <section class="poster" style="left:377px;top:20px;width:333px;height:452px">
    <div class="photo" role="img" aria-label="Foto: Frau räumt mit zwei Kleinkindern Spielzeug in einen Korb" style="left:0;top:170px;width:333px;height:200px;background:linear-gradient(135deg,#eeeeee,#d5d8dc 55%,#c9ccd6)"></div>
    <svg class="shapes" viewBox="0 0 333 452" aria-hidden="true">
      <path d="M0,98 C90,72 230,70 333,86 L333,178 C240,192 110,170 0,190 Z" fill="var(--charcoal)"/>
      <path d="M0,186 C110,168 240,188 333,174 L333,180 C240,194 110,174 0,194 Z" fill="var(--red)"/>
      <path d="M0,352 C120,320 230,338 333,300 L333,322 C230,356 120,336 0,366 Z" fill="var(--sweep)"/>
      <path d="M0,366 C120,336 230,356 333,322 L333,452 L0,452 Z" fill="var(--red)"/>
    </svg>
    <div class="brand" style="left:50px;top:22px"><span class="brand-mark"></span><div><div class="brand-name">LINDWERK</div><div class="brand-sub">HAUSHALTSHILFEN &amp; MEHR</div></div></div>
    <div class="headline" style="top:106px">KOSTENLOSE<br>HAUSHALTSHILFE AB<br>PFLEGEGRAD 1</div>
    <div class="cta" style="top:380px">
      <div class="cta-label">Buchen Sie gleich einen Termin:</div>
      <div class="phone"><svg class="phone-icon" viewBox="0 0 20 20"><circle cx="10" cy="10" r="10" fill="#fff"/><path d="M6.2,5.2l2,-.4 1.2,2.6-1.3,1c.6,1.3 1.6,2.3 2.9,2.9l1-1.3 2.6,1.2-.4,2c-4.5,.3-8.3,-3.5-8,-8z" fill="var(--red)"/></svg>0711 98 76 54 32</div>
      <div class="url">www.lindwerk-hilfe.de</div>
    </div>
  </section>

  <section class="poster" style="left:732px;top:20px;width:333px;height:452px">
    <div class="photo" role="img" aria-label="Foto: Mutter und Tochter mit Wäsche vor einer Waschmaschine" style="left:0;top:170px;width:333px;height:200px;background:linear-gradient(135deg,#f4f4f4,#dcdcdc 50%,#b9c3c9)"></div>
    <svg class="shapes" viewBox="0 0 333 452" aria-hidden="true">
      <path d="M0,98 C90,72 230,70 333,86 L333,178 C240,192 110,170 0,190 Z" fill="var(--charcoal)"/>
      <path d="M0,186 C110,168 240,188 333,174 L333,180 C240,194 110,174 0,194 Z" fill="var(--red)"/>
      <path d="M0,352 C120,320 230,338 333,300 L333,322 C230,356 120,336 0,366 Z" fill="var(--sweep)"/>
      <path d="M0,366 C120,336 230,356 333,322 L333,452 L0,452 Z" fill="var(--red)"/>
    </svg>
    <div class="brand" style="left:50px;top:22px"><span class="brand-mark"></span><div><div class="brand-name">LINDWERK</div><div class="brand-sub">HAUSHALTSHILFEN &amp; MEHR</div></div></div>
    <div class="headline" style="top:118px">ABRECHNUNG MIT<br>ALLEN KOSTENTRÄGERN</div>
    <div class="cta" style="top:380px">
      <div class="cta-label">Buchen Sie gleich einen Termin:</div>
      <div class="phone"><svg class="phone-icon" viewBox="0 0 20 20"><circle cx="10" cy="10" r="10" fill="#fff"/><path d="M6.2,5.2l2,-.4 1.2,2.6-1.3,1c.6,1.3 1.6,2.3 2.9,2.9l1-1.3 2.6,1.2-.4,2c-4.5,.3-8.3,-3.5-8,-8z" fill="var(--red)"/></svg>0711 98 76 54 32</div>
      <div class="url">www.lindwerk-hilfe.de</div>
    </div>
  </section>
</div>

<!-- bottom row -->
<div class="frame frame-bottom-ext"></div>
<div class="frame frame-bottom">

  <div class="panel" style="left:22px;top:20px;width:333px;height:535px">
    <section class="poster" style="left:0;top:67px;width:333px;height:403px">
      <div class="photo" role="img" aria-label="Foto: lächelnde Frau mit Schürze und gelben Handschuhen putzt einen Tisch" style="left:150px;top:70px;width:183px;height:270px;background:linear-gradient(160deg,#e9e2d8,#c9b6a0 55%,#9fb4c8)"></div>
      <svg class="shapes" viewBox="0 0 333 403" aria-hidden="true">
        <path d="M0,0 L333,0 L333,82 C250,96 150,66 0,102 Z" fill="var(--red)"/>
        <path d="M0,102 C150,66 250,96 333,82 L333,88 C250,102 150,72 0,108 Z" fill="var(--charcoal)"/>
        <path d="M0,372 C100,350 220,340 333,322 L333,340 C220,358 100,368 0,388 Z" fill="var(--sweep)"/>
        <path d="M80,403 C150,370 250,360 333,336 L333,403 Z" fill="var(--red)"/>
      </svg>
      <div class="brand on-red" style="left:48px;top:14px"><span class="brand-mark"></span><div><div class="brand-name">LINDWERK</div><div class="brand-sub">HAUSHALTSHILFEN &amp; MEHR</div></div></div>
      <div class="lead" style="left:22px;top:130px;font-size:14.5px">BIETEN WIR<br>IHNEN BEDARFS-<br>ORIENTIERTE<br>HILFE RUND<br>UM DEN<br>HAUSHALT AN.</div>
      <div class="small" style="left:22px;top:240px;width:100px">Mit unserem breiten Spektrum an Services möchten wir Sie beim bewältigen des Alltags unterstützen.</div>
      <div class="script" style="left:28px;top:318px;font-size:17px">Wir Sind<br>für Sie da!</div>
      <div class="url" style="position:absolute;left:120px;top:380px;color:#fff">www.lindwerk-hilfe.de</div>
    </section>
  </div>

  <div class="panel" style="left:377px;top:20px;width:333px;height:742px">
    <section class="poster" style="left:0;top:155px;width:333px;height:434px">
      <svg class="shapes" viewBox="0 0 333 434" aria-hidden="true">
        <path d="M0,0 L333,0 L333,40 C240,14 110,10 0,30 Z" fill="var(--red)"/>
        <path d="M0,30 C110,10 240,14 333,40 L333,48 C240,22 110,18 0,38 Z" fill="var(--sweep)"/>
        <path d="M0,410 C120,404 240,380 333,350 L333,372 C240,400 120,418 0,422 Z" fill="var(--sweep)"/>
        <path d="M0,418 C120,412 240,392 333,366 L333,434 L0,434 Z" fill="var(--red)"/>
      </svg>
      <div style="position:absolute;left:96px;top:62px;width:140px;height:140px;border-radius:50%;border:10px solid var(--red)"></div>
      <div style="position:absolute;left:0;right:0;top:206px;text-align:center;font-family:'Cinzel',serif;font-weight:600;font-size:42px;color:var(--ink);line-height:1">LINDWERK</div>
      <div style="position:absolute;left:0;right:0;top:250px;text-align:center;font-family:'Cinzel',serif;font-weight:600;font-size:15px;color:var(--red);letter-spacing:.6px">HAUSHALTSHILFEN &amp; MEHR</div>
      <div style="position:absolute;left:0;right:0;top:282px;text-align:center;font-size:9px;font-weight:500;color:var(--red)">Buchen Sie gleich einen Termin:</div>
      <div style="position:absolute;left:53px;top:296px;width:227px;height:40px;border:3px solid var(--red);border-radius:20px;display:flex;align-items:center;justify-content:center;gap:6px;font-weight:700;font-size:25px;color:var(--ink)"><svg class="phone-icon" viewBox="0 0 20 20"><circle cx="10" cy="10" r="10" fill="var(--red)"/><path d="M6.2,5.2l2,-.4 1.2,2.6-1.3,1c.6,1.3 1.6,2.3 2.9,2.9l1-1.3 2.6,1.2-.4,2c-4.5,.3-8.3,-3.5-8,-8z" fill="#fff"/></svg>0711 98 76 54 32</div>
      <div style="position:absolute;left:54px;top:346px;display:flex;gap:5px;font-size:10px;line-height:1.3;color:var(--ink)"><svg width="10" height="13" viewBox="0 0 10 13"><path d="M5,0C2.2,0 0,2.2 0,5c0,3.5 5,8 5,8s5,-4.5 5,-8C10,2.2 7.8,0 5,0z" fill="var(--red)"/><circle cx="5" cy="5" r="1.8" fill="#fff"/></svg><div>Firma Lindwerk, Sabine Korte<br>Lindenstraße 14, 70173 Stuttgart</div></div>
      <div class="url" style="position:absolute;left:135px;top:410px;color:#fff">www.lindwerk-hilfe.de</div>
    </section>
  </div>

  <div class="panel" style="left:732px;top:20px;width:333px;height:535px">
    <section class="poster" style="left:0;top:67px;width:333px;height:403px">
      <div class="photo" role="img" aria-label="Foto: Frau in blauer Schürze wischt mit einem Mopp den Boden" style="left:200px;top:80px;width:133px;height:290px;background:linear-gradient(180deg,#7ea8d8,#3e7cc8 50%,#e8e4de)"></div>
      <svg class="shapes" viewBox="0 0 333 403" aria-hidden="true">
        <path d="M0,0 L333,0 L333,80 C230,78 110,70 0,100 Z" fill="var(--red)"/>
        <path d="M0,372 C100,350 220,345 333,310 L333,330 C220,362 100,368 0,388 Z" fill="var(--sweep)"/>
        <path d="M0,385 C100,365 220,360 333,326 L333,403 L0,403 Z" fill="var(--red)"/>
      </svg>
      <div class="brand on-red" style="left:48px;top:14px"><span class="brand-mark"></span><div class="brand-name">LINDWERK</div></div>
      <div class="lead" style="left:27px;top:118px;font-size:16px">BENÖTIGEN HILFE<br>IM HAUSHALT?</div>
      <div style="position:absolute;left:27px;top:157px;font-family:'Cinzel',serif;font-weight:700;font-size:9.5px;color:var(--ink);line-height:1.15">JETZT KOSTENLOS BERATEN<br>LASSEN!</div>
      <div style="position:absolute;left:27px;top:186px;width:170px;height:1px;background:var(--red)"></div>
      <div style="position:absolute;left:27px;top:196px">
        <div class="contact-label">FESTNETZ:</div>
        <div class="contact-num"><svg class="phone-icon" viewBox="0 0 20 20" style="width:17px;height:17px"><circle cx="10" cy="10" r="10" fill="var(--red)"/><path d="M6.2,5.2l2,-.4 1.2,2.6-1.3,1c.6,1.3 1.6,2.3 2.9,2.9l1-1.3 2.6,1.2-.4,2c-4.5,.3-8.3,-3.5-8,-8z" fill="#fff"/></svg>0711 98 76 54 32</div>
        <div class="contact-label" style="margin-top:14px">24/7 MOBIL:</div>
        <div class="contact-num"><svg class="phone-icon" viewBox="0 0 20 20" style="width:17px;height:17px"><circle cx="10" cy="10" r="10" fill="var(--red)"/><path d="M6.2,5.2l2,-.4 1.2,2.6-1.3,1c.6,1.3 1.6,2.3 2.9,2.9l1-1.3 2.6,1.2-.4,2c-4.5,.3-8.3,-3.5-8,-8z" fill="#fff"/></svg>0711 98 76 54 32</div>
        <div style="font-size:11px;font-weight:700;color:var(--red);margin-top:6px">www.lindwerk-hilfe.de</div>
      </div>
    </section>
  </div>
</div>

</body>
</html>
```